Dorin Commercial Truck / Trailer / RV Repair

Need a billboard design for our shop. Will include our logo below and want the word DORIN on the top without the circle. Straighten out the letter "M" on the logo as well. Also will include a rough draft of a design and words I had in mind. All the words need to be included but the layout and design is up to you. Open to all options just needs to be easy to see and understand the message from the highway.

```html
<!DOCTYPE html>
<html lang="en">
<head>
<meta charset="utf-8">
<title>Dorin Commercial Repair Shop Billboard</title>
<link rel="stylesheet" href="https://fonts.googleapis.com/css2?family=Montserrat:wght@600;700&family=Roboto+Condensed:wght@500;700&display=swap">
<style>
  :root {
    --brand-blue: #3f8bcd;
    --brand-gray: #6d6a66;
    --label-gray: #5f5c59;
    --panel-white: #ffffff;
    --page-bg: #e9eaec;
    --photo-light: #eef0f2;
    --photo-mid: #c9ced4;
    --truck-blue: #4f7fc9;
  }
  html, body {
    margin: 0;
    width: 1200px;
    height: 800px;
    overflow: hidden;
    background: var(--page-bg);
  }
  .canvas {
    position: relative;
    width: 1200px;
    height: 800px;
  }
  .billboard {
    position: absolute;
    left: 20px;
    top: 140px;
    width: 1160px;
    height: 520px;
    box-shadow: 0 6px 18px rgba(0,0,0,0.18);
  }
  .bg-blue { fill: var(--brand-blue); }
  .panel-white { fill: var(--panel-white); }
  .band-gray { fill: var(--brand-gray); }
  .brand-name {
    font-family: "Montserrat", sans-serif;
    font-weight: 700;
    fill: var(--brand-blue);
  }
  .headline {
    font-family: "Montserrat", sans-serif;
    font-weight: 700;
    fill: var(--panel-white);
  }
  .service-label {
    font-family: "Roboto Condensed", sans-serif;
    font-weight: 700;
    fill: var(--label-gray);
  }
  .service-label--light { fill: var(--panel-white); font-family: "Montserrat", sans-serif; }
  .parking-line {
    font-family: "Montserrat", sans-serif;
    font-weight: 700;
    fill: var(--panel-white);
  }
  .call-word, .call-note {
    font-family: "Roboto Condensed", sans-serif;
    font-weight: 500;
    fill: var(--panel-white);
  }
  .phone-number {
    font-family: "Roboto Condensed", sans-serif;
    font-weight: 700;
    fill: var(--panel-white);
  }
</style>
</head>
<body>
<div class="canvas">
  <svg class="billboard" viewBox="0 0 1160 520" xmlns="http://www.w3.org/2000/svg">
    <defs>
      <linearGradient id="vehicle-light" x1="0" y1="0" x2="0" y2="1">
        <stop offset="0" stop-color="var(--photo-light)"/>
        <stop offset="1" stop-color="var(--photo-mid)"/>
      </linearGradient>
      <linearGradient id="vehicle-blue" x1="0" y1="0" x2="0" y2="1">
        <stop offset="0" stop-color="var(--truck-blue)"/>
        <stop offset="1" stop-color="var(--photo-mid)"/>
      </linearGradient>
    </defs>

    <!-- base -->
    <rect class="bg-blue" x="0" y="0" width="1160" height="520"/>

    <!-- brand panel -->
    <polygon class="panel-white" points="0,0 560,0 500,190 0,190"/>
    <text class="brand-name" x="36" y="150" font-size="132" textLength="430" lengthAdjust="spacingAndGlyphs">DORIN</text>

    <!-- headline -->
    <text class="headline" x="585" y="92" font-size="48" textLength="555" lengthAdjust="spacingAndGlyphs">COMMERCIAL REPAIR SHOP</text>

    <!-- RV service -->
    <g role="img" aria-label="Photo of a white motorhome RV">
      <rect x="40" y="215" width="300" height="165" rx="6" fill="url(#vehicle-light)"/>
    </g>
    <text class="service-label service-label--light" x="372" y="372" font-size="58">RV</text>

    <!-- trailers panel -->
    <polygon class="panel-white" points="590,125 880,125 850,395 500,395"/>
    <g role="img" aria-label="Photo of a white semi truck pulling a box trailer">
      <rect x="560" y="205" width="250" height="175" rx="6" fill="url(#vehicle-light)"/>
    </g>
    <text class="service-label" x="730" y="178" font-size="34">TRAILERS</text>

    <!-- trucks panel -->
    <polygon class="panel-white" points="900,125 1160,125 1160,395 870,395"/>
    <g role="img" aria-label="Photo of a blue semi truck cab">
      <rect x="1000" y="150" width="148" height="230" rx="6" fill="url(#vehicle-blue)"/>
    </g>
    <text class="service-label" x="890" y="375" font-size="32">TRUCKS</text>

    <!-- parking band -->
    <polygon class="band-gray" points="0,400 650,400 610,520 0,520"/>
    <text class="parking-line" x="32" y="476" font-size="38" textLength="555" lengthAdjust="spacingAndGlyphs">PARKING AND STORAGE AVAILABLE</text>

    <!-- call to action -->
    <text class="call-word" x="650" y="478" font-size="32">CALL</text>
    <text class="phone-number" x="718" y="486" font-size="70" textLength="300" lengthAdjust="spacingAndGlyphs">888.555.0142</text>
    <text class="call-note" x="1032" y="458" font-size="21">OR COME BY</text>
    <text class="call-note" x="1032" y="486" font-size="21">FOR A QUOTE!</text>
  </svg>
</div>
</body>
</html>
```